CONTACT US Page and design for website

We need a contact us page for our website. We would like it to have a message area, a map, our information, etc.

Please see the text attachment for what we are looking for. We need to have something that is creative and interesting, modern and professional.

We believe that a contact US page should be very creative because everyone clicks that to contact us. We want it to be super professional, attention grabbing, pleasing to the eye.

PLEASE KEEP THE HEADER AND FOOTER THE SAME, ONLY THE ACTUAL CONTACT US PAGE NEEDS TO BE WORKED ON. THANKS!
We are excited to work with designers for this project.

Target Market(s)

Clients in technology business

Industry/Entity Type

Information Technology

Number of Pages Required

1 page

Font styles to use
Serif

Requirements
Must have
• CHECK THE TEXT ATTACHMENT PLEASE
• Must stay within our design colors and theme.
Nice to have
• see attachment
Should not have
• it should be special

```html
<!DOCTYPE html>
<html lang="en">
<head>
<meta charset="utf-8">
<title>Contact Us – Novix Tech</title>
<link rel="stylesheet" href="https://fonts.googleapis.com/css2?family=Open+Sans:wght@400;600;700&display=swap">
<style>
:root{
  --teal:#26b0a5;
  --teal-dark:#1e968c;
  --ink:#555;
  --ink-soft:#888;
  --page:#f3f3f3;
  --white:#fff;
  --line:#dcdcdc;
  --footer:#a8a8a8;
  --footer-dark:#8e8e8e;
  --map:#cfd2d4;
  --photo-light:#ddd3c0;
  --photo-gold:#d4b36e;
}
*{box-sizing:border-box;margin:0;padding:0}
html,body{width:1200px;height:2372px;overflow:hidden}
body{position:relative;background:var(--page);font-family:"Open Sans",Arial,sans-serif;color:var(--ink)}
/* header */
.site-header{position:absolute;left:0;top:0;width:1200px;height:138px;background:var(--white);border-bottom:3px solid var(--teal)}
.brand{position:absolute;left:90px;top:20px;display:flex;align-items:center;gap:14px}
.brand-mark{width:52px;height:52px;border-radius:50%;background:var(--teal)}
.brand-name{font-size:40px;font-weight:700;color:var(--teal);letter-spacing:1px}
.account-tabs{position:absolute;left:922px;top:0;width:148px;height:26px;background:#999;border-radius:0 0 14px 14px;display:flex;justify-content:space-around;align-items:center;font-size:10px;color:var(--white)}
.header-contact{position:absolute;top:44px;display:flex;align-items:center;gap:12px;font-size:14px;color:var(--ink)}
.icon-circle{width:38px;height:38px;border-radius:50%;border:1px solid var(--line);display:flex;align-items:center;justify-content:center}
.main-nav{position:absolute;left:90px;top:106px;display:flex;gap:26px;font-size:11px;font-weight:600;color:var(--ink)}
.search{position:absolute;left:897px;top:102px;width:152px;height:32px;border:1px solid #bbb;border-radius:16px;font-size:11px;padding:8px 16px;color:#666}
.search svg{position:absolute;right:12px;top:8px}
.cart{position:absolute;left:1062px;top:102px;width:32px;height:32px;border-radius:50%;border:1px solid #bbb;display:flex;align-items:center;justify-content:center}
/* map */
.map-frame{position:absolute;left:88px;top:192px;width:1006px;height:338px;background:var(--white);padding:6px}
.map{width:100%;height:100%;background:linear-gradient(135deg,#d7d9db,#c5c8ca)}
.map-card{position:absolute;left:438px;top:68px;width:238px;height:114px;background:var(--white);padding:16px 14px;font-size:11px;line-height:20px;box-shadow:0 1px 4px rgba(0,0,0,.2)}
.map-card .name{color:var(--teal);font-weight:600}
.map-card .mark{position:absolute;right:22px;top:30px;width:52px;height:52px;border-radius:50%;background:var(--teal)}
/* get in touch */
.section-title{position:absolute;left:0;width:1200px;text-align:center;font-weight:700;letter-spacing:1px}
.intro{position:absolute;left:0;width:1200px;text-align:center;font-size:14px;line-height:26px;color:var(--ink-soft)}
.info-card{position:absolute;top:738px;width:228px;height:160px;background:var(--white);border:1px solid #e4e4e4;padding:20px 16px}
.info-card h3{font-size:14px;font-weight:600;color:var(--teal);margin-bottom:16px}
.info-row{display:flex;align-items:center;gap:10px;font-size:14px;margin-bottom:14px}
.dot{width:24px;height:24px;border-radius:50%;background:var(--teal);display:flex;align-items:center;justify-content:center;flex:none}
.social{display:flex;gap:10px;margin-top:6px}
.social span{width:42px;height:42px;border-radius:50%;border:2px solid var(--teal)}
/* contact form */
.contact-band{position:absolute;left:0;top:944px;width:1200px;height:555px;background:var(--teal);color:var(--white)}
.field{position:absolute;background:var(--white);border-radius:4px;font-size:15px;color:#777;padding:12px 16px;display:flex;gap:10px;align-items:flex-start}
.submit{position:absolute;left:980px;top:458px;width:118px;height:48px;border:2px solid var(--white);border-radius:4px;font-size:16px;font-weight:700;display:flex;align-items:center;justify-content:center;letter-spacing:1px}
/* hours */
.hours-list{position:absolute;left:301px;top:1718px;font-size:15px;line-height:33px;color:var(--ink)}
.clocks-photo{position:absolute;left:580px;top:1660px;width:380px;height:272px;background:linear-gradient(90deg,var(--photo-light),var(--photo-gold))}
/* footer */
.site-footer{position:absolute;left:0;top:1940px;width:1200px;height:290px;background:var(--footer);color:var(--white)}
.footer-about{position:absolute;left:380px;top:14px;width:440px;text-align:center;font-size:13px;line-height:20px}
.footer-contact{position:absolute;top:132px;display:flex;gap:8px;font-size:14px;line-height:20px}
.footer-links{position:absolute;top:190px;font-size:15px;font-weight:600}
.footer-sub{font-size:10px;font-weight:400;line-height:13px;margin-top:4px;padding-left:22px}
.footer-bottom{position:absolute;left:0;top:2230px;width:1200px;height:142px;background:var(--footer-dark);color:var(--white);text-align:center}
.footer-social{display:flex;gap:16px;justify-content:center;margin-top:22px}
.footer-social span{width:34px;height:34px;border-radius:50%;border:1px solid var(--white)}
.footer-rule{width:820px;height:1px;background:#b5b5b5;margin:20px auto 12px}
.footer-brand{font-size:13px;line-height:17px}
</style>
</head>
<body>

<header class="site-header">
  <div class="brand"><span class="brand-mark"></span><span class="brand-name">NOVIXTECH</span></div>
  <div class="account-tabs"><span>SIGN UP</span><span>LOGIN</span></div>
  <div class="header-contact" style="left:806px"><span class="icon-circle"><svg width="18" height="16"><path d="M2 2h14v9H8l-4 3v-3H2z" fill="var(--teal)"/></svg></span>LIVE CHAT</div>
  <div class="header-contact" style="left:936px;font-size:19px"><span class="icon-circle"><svg width="16" height="16"><path d="M3 1l3 3-2 2c1 2 3 4 5 5l2-2 3 3-2 2C7 14 2 9 1 3z" fill="var(--teal)"/></svg></span>555-014-3013</div>
  <nav class="main-nav"><span>SERVERS</span><span>WORKSTATIONS</span><span>COMPONENTS</span><span>VIRTUAL REALITY</span><span>DRONES</span><span>ABOUT US</span><span>BLOG</span><span>RESOURCES</span><span>CONTACT US</span></nav>
  <div class="search">Search<svg width="14" height="14"><circle cx="6" cy="6" r="4.5" fill="none" stroke="var(--teal)" stroke-width="2"/><path d="M9.5 9.5l3.5 3.5" stroke="var(--teal)" stroke-width="2"/></svg></div>
  <div class="cart"><svg width="16" height="14"><path d="M1 1h3l2 8h8l2-6H5" fill="none" stroke="var(--teal)" stroke-width="1.6"/><circle cx="7" cy="12" r="1.3" fill="var(--teal)"/><circle cx="13" cy="12" r="1.3" fill="var(--teal)"/></svg></div>
</header>

<div class="map-frame">
  <div class="map" role="img" aria-label="Street map showing the office location"></div>
  <div class="map-card"><div class="name">Novix Tech, LLC.</div>4820 Larkin Ave.<br>Millbrook, CA 91000<span class="mark"></span></div>
</div>

<h1 class="section-title" style="top:582px;font-size:36px;color:#666">GET IN TOUCH</h1>
<p class="intro" style="top:640px">Duis sed odio sit amet nibh vulputate cursus a sit amet mauris. Morbi accumsan<br>ipsuy velit. Nam nec tellus a odio tincidunt auctor</p>

<section class="info-card" style="left:114px"><h3>GENERAL INQUIRIES</h3>
  <div class="info-row"><span class="dot"><svg width="12" height="12"><path d="M2 1l2 2-1 2c1 1 2 2 4 3l1-1 2 2-1 2C5 11 1 7 1 3z" fill="#fff"/></svg></span>(555)014-3013</div>
  <div class="info-row"><span class="dot"><svg width="12" height="10"><rect x="1" y="1" width="10" height="8" fill="#fff"/><path d="M1 1l5 4 5-4" stroke="var(--teal)" fill="none"/></svg></span>info@novixtech.com</div></section>
<section class="info-card" style="left:363px"><h3>SALES INQUIRIES</h3>
  <div class="info-row"><span class="dot"><svg width="12" height="12"><path d="M2 1l2 2-1 2c1 1 2 2 4 3l1-1 2 2-1 2C5 11 1 7 1 3z" fill="#fff"/></svg></span>(555)014-3013</div>
  <div class="info-row"><span class="dot"><svg width="12" height="10"><rect x="1" y="1" width="10" height="8" fill="#fff"/><path d="M1 1l5 4 5-4" stroke="var(--teal)" fill="none"/></svg></span>sales@novixtech.com</div></section>
<section class="info-card" style="left:612px"><h3>PURCHASING INQUIRIES</h3>
  <div class="info-row"><span class="dot"><svg width="12" height="12"><path d="M2 1l2 2-1 2c1 1 2 2 4 3l1-1 2 2-1 2C5 11 1 7 1 3z" fill="#fff"/></svg></span>(555)014-3014</div>
  <div class="info-row"><span class="dot"><svg width="12" height="10"><rect x="1" y="1" width="10" height="8" fill="#fff"/><path d="M1 1l5 4 5-4" stroke="var(--teal)" fill="none"/></svg></span>purchasing@novixtech.com</div></section>
<section class="info-card" style="left:861px"><h3>STAY CONNECTED</h3>
  <div class="social"><span></span><span></span><span></span><span></span></div></section>

<section class="contact-band">
  <h2 class="section-title" style="top:46px;font-size:36px;color:var(--white)">CONTACT US</h2>
  <p class="intro" style="top:104px;color:var(--white);font-size:14px;line-height:24px">We are here to answer any questions you may have.<br>Send us a message and we will respond as soon as possible.</p>
  <div class="field" style="left:128px;top:197px;width:304px;height:47px">&#9679; Name</div>
  <div class="field" style="left:458px;top:197px;width:304px;height:47px">&#9993; Email</div>
  <div class="field" style="left:787px;top:197px;width:304px;height:47px">&#9990; Phone Number</div>
  <div class="field" style="left:128px;top:270px;width:963px;height:146px">&#9635; Message</div>
  <div class="submit">SUBMIT</div>
</section>

<h2 class="section-title" style="top:1546px;font-size:34px;color:#666">HOURS OF OPERATION</h2>
<p class="intro" style="top:1598px;font-size:17px;line-height:30px;color:#666">Our dedicated customer service representatives are<br><span style="color:var(--teal)">available 24/7 by phone.</span></p>
<div class="hours-list">Monday: 8:00am- 5:00pm<br>Tuesday: 8:00am- 5:00pm<br>Wednesday: 8:00am- 5:00pm<br>Thursday: 8:00am- 5:00pm<br>Friday: 8:00am- 5:00pm</div>
<div class="clocks-photo" role="img" aria-label="Photo of two brass alarm clocks"></div>

<footer class="site-footer">
  <p class="footer-about">Based in Millbrook California, Novix Tech offers custom servers, storage, and workstations for local businesses in Los Angeles, Beverly Hills, Thousand Oaks, Ventura, Orange County, Santa Barbara, Oxnard, Irvine, Anaheim, and San Diego. Novix Tech also offers such products to clients throughout the United States and Worldwide.</p>
  <div class="footer-contact" style="left:376px"><span>&#9679;</span><span>4820 Larkin Ave.<br>Millbrook, CA 91000</span></div>
  <div class="footer-contact" style="left:546px"><span>&#9990;</span><span>555-014-3013</span></div>
  <div class="footer-contact" style="left:690px"><span>&#9993;</span><span>sales@novixtech.com</span></div>
  <div class="footer-links" style="left:344px">Servers</div>
  <div class="footer-links" style="left:472px">Drones</div>
  <div class="footer-links" style="left:562px">Graphics</div>
  <div class="footer-links" style="left:666px">About</div>
  <div class="footer-links" style="left:750px">Customer Support
    <div class="footer-sub">Terms and Conditions<br>Warranty Information<br>Contact Us<br>Return Policy</div></div>
</footer>

<div class="footer-bottom">
  <div class="footer-social"><span></span><span></span><span></span><span></span></div>
  <div class="footer-rule"></div>
  <div class="footer-brand">Novix Tech, LLC.<br>Copyright © 2017</div>
</div>

</body>
</html>
```